VKTO Meridian LLC Website

Basic website for a start up business in the defense and federal space. If we could have intelligence analysis and technology as a focus that would be great. Looking to use our core colors but a lighter set of web pages would be preferable

Target Market(s)

Defense

Coding

Coded - Design and coding required

Number of Pages Required

3 page

```html
<!DOCTYPE html>
<html lang="en">
<head>
<meta charset="utf-8">
<title>VKTO Meridian — Defense and Federal Space</title>
<link rel="stylesheet" href="https://fonts.googleapis.com/css2?family=Audiowide&family=Poppins:wght@400;500;600;700&display=swap">
<style>
:root{
  --red:#c8002f;
  --red-dark:#a60027;
  --ink:#15151a;
  --ink-soft:#2a2a30;
  --text:#555a60;
  --muted:#8a8f95;
  --line:#e2e2e4;
  --white:#ffffff;
  --paper:#f4f4f5;
}
*{box-sizing:border-box;margin:0;padding:0}
html,body{width:1200px;height:4300px;overflow:hidden}
body{position:relative;background:var(--white);font-family:"Poppins",sans-serif;color:var(--text)}
.abs{position:absolute}
.display{font-family:"Audiowide",sans-serif;color:var(--ink);text-transform:uppercase;letter-spacing:1px}
a{color:inherit;text-decoration:none}

/* header */
.site-header{position:absolute;left:0;top:0;width:1200px;height:100px;z-index:5}
.brand{position:absolute;left:88px;top:28px;display:flex;align-items:center;gap:12px;font-family:"Poppins",sans-serif;font-weight:700;font-size:30px;color:var(--white);letter-spacing:2px}
.brand-mark{width:14px;height:14px;background:var(--red)}
.main-nav{position:absolute;right:148px;top:41px;display:flex;gap:27px;font-size:13px;font-weight:500;color:var(--white)}
.main-nav .active{color:var(--red)}
.search-btn{position:absolute;right:92px;top:31px;width:38px;height:38px;border-radius:50%;background:#3a3a40}

/* hero */
.hero-bg{position:absolute;left:0;top:0;z-index:0}
.hero-photo{position:absolute;left:500px;top:90px;width:700px;height:520px;background:radial-gradient(ellipse at 60% 40%,rgba(40,150,140,.55),rgba(60,70,60,.35) 45%,rgba(20,20,26,0) 75%);z-index:1}
.hero-copy{position:absolute;left:88px;top:205px;z-index:2}
.hero-title{font-family:"Audiowide",sans-serif;font-size:66px;line-height:72px}
.hero-title .red{color:var(--red)}
.hero-title .white{color:var(--white)}
.hero-sub{font-family:"Audiowide",sans-serif;color:var(--white);font-size:20px;letter-spacing:1px;margin-top:6px}
.hero-text{color:#e2e2e4;font-size:14px;line-height:23px;width:400px;margin-top:18px}
.btn{display:inline-block;font-size:11px;font-weight:700;text-transform:uppercase;text-align:center}
.btn-red{background:var(--red);color:var(--white);width:188px;height:42px;line-height:42px;margin-top:26px}

/* about */
.about-frame{position:absolute;left:175px;top:656px;width:392px;height:549px;background:var(--white);box-shadow:0 8px 30px rgba(0,0,0,.12);z-index:3}
.about-photo{position:absolute;left:10px;top:10px;width:372px;height:539px;background:linear-gradient(160deg,#8fb7cc 0%,#5c7a6a 35%,#c89a4a 60%,#2c3a44 100%)}
.about-copy{position:absolute;left:648px;top:818px;width:380px}
.eyebrow{color:var(--red);font-family:"Audiowide",sans-serif;font-size:13px;letter-spacing:1px}
.section-title-left{font-size:31px;line-height:36px;margin-top:12px}
.about-text{font-size:13.5px;line-height:22.3px;margin-top:16px}
.btn-grey{background:#e6e6e8;color:var(--ink);width:134px;height:36px;line-height:36px;margin-top:24px}

/* applications */
.section-title{position:absolute;left:0;width:1200px;text-align:center;font-size:33px}
.app-accent{position:absolute;left:726px;top:1577px;width:474px;height:267px;background:var(--red)}
.app-card{position:absolute;top:1362px;width:246px;height:380px;background:var(--white);box-shadow:0 6px 22px rgba(0,0,0,.08)}
.app-photo{height:215px}
.app-body{position:relative;padding:20px 24px 0 24px}
.app-body::before{content:"";position:absolute;left:0;top:22px;width:3px;height:22px;background:var(--red)}
.app-name{font-family:"Audiowide",sans-serif;color:var(--ink);font-size:15px}
.app-text{font-size:12px;line-height:18px;margin-top:12px}
.read-more{display:inline-block;margin-top:16px;font-size:11px;font-weight:600;color:var(--muted);border-bottom:1px solid var(--muted)}
.slider-btn{position:absolute;top:1774px;width:32px;height:38px;background:#e03a5c}
.slider-track{position:absolute;left:832px;top:1793px;width:262px;height:1px;background:rgba(255,255,255,.5)}

/* banner */
.banner{position:absolute;left:0;top:1844px;width:1200px;height:743px;background:linear-gradient(180deg,#7e9fbe 0%,#a9bfd3 45%,#c9c2b4 70%,#a88a56 85%,#6d5a3a 100%)}
.banner-title{position:absolute;left:88px;top:1958px;font-family:"Audiowide",sans-serif;color:var(--white);font-size:54px;line-height:54px}
.banner-sub{position:absolute;left:88px;top:2134px;font-family:"Audiowide",sans-serif;color:var(--white);font-size:16px;line-height:21px}
.btn-white{position:absolute;left:88px;top:2203px;width:134px;height:36px;line-height:36px;background:var(--white);color:var(--ink)}

/* work with us */
.work-text{position:absolute;left:280px;top:2660px;width:640px;text-align:center;font-size:14px;line-height:24px}
.work-item{position:absolute;top:2729px;width:190px;text-align:center}
.work-circle{width:150px;height:150px;border-radius:50%;margin:0 auto;display:flex;align-items:center;justify-content:center}
.work-circle.red{background:var(--red)}
.work-circle.dark{background:var(--ink)}
.work-label{font-family:"Audiowide",sans-serif;color:var(--ink);font-size:14px;line-height:16px;margin-top:16px}
.divider{position:absolute;left:88px;top:2991px;width:1022px;height:1px;background:var(--line)}

/* blog */
.blog-card{position:absolute;top:3096px;width:277px;height:396px;background:var(--white);box-shadow:0 6px 24px rgba(0,0,0,.09);padding:10px}
.blog-photo{height:197px}
.blog-body{padding:18px 12px 0}
.blog-date{font-size:11px;color:var(--muted)}
.blog-title{font-size:16px;font-weight:600;color:var(--ink);margin-top:8px}
.blog-text{font-size:12px;line-height:18px;margin-top:8px}
.blog-link{display:block;text-align:center;border-top:1px solid var(--line);margin-top:16px;padding-top:12px;font-size:11px;font-weight:600;color:var(--muted)}

/* newsletter */
.newsletter{position:absolute;left:88px;top:3557px;width:1022px;height:188px;background:var(--red);z-index:3}
.newsletter-title{position:absolute;left:62px;top:40px;font-family:"Audiowide",sans-serif;color:var(--white);font-size:34px;line-height:38px}
.newsletter-text{position:absolute;left:62px;top:128px;color:var(--white);font-size:15px}
.subscribe-form{position:absolute;left:479px;top:71px;width:482px;height:45px;background:var(--white);border:3px solid var(--white);display:flex;align-items:center}
.subscribe-input{flex:1;padding-left:42px;font-size:14px;color:var(--ink-soft);position:relative}
.subscribe-btn{width:120px;height:39px;line-height:39px;background:var(--ink);color:var(--white);text-align:center;font-size:12px;font-weight:700}

/* footer */
.footer-bg{position:absolute;left:0;top:3680px;z-index:1}
.footer-brand{position:absolute;left:88px;top:3998px;display:flex;align-items:center;gap:12px;color:var(--white);font-weight:700;font-size:34px;letter-spacing:2px;z-index:2}
.footer-col{position:absolute;top:3893px;z-index:2;color:#d7d7da}
.footer-head{font-family:"Audiowide",sans-serif;color:var(--white);font-size:16px;margin-bottom:18px}
.footer-links li{list-style:none;font-size:12.5px;line-height:26.7px}
.contact-item{position:relative;padding-left:24px;font-size:12.5px;line-height:19px;margin-bottom:24px}
.contact-item svg{position:absolute;left:0;top:3px}
.socials{display:flex;gap:12px}
.social{width:46px;height:46px;border-radius:50%;background:#2e2e34;border:1px solid #45454c}
.footer-rule{position:absolute;left:88px;top:4234px;width:1022px;height:1px;background:#35353b;z-index:2}
.copyright{position:absolute;left:0;top:4256px;width:1200px;text-align:center;color:var(--white);font-size:13px;font-weight:500;z-index:2}
.chat-btn{position:absolute;left:1131px;top:4210px;width:48px;height:48px;border-radius:50%;background:var(--red);z-index:3;display:flex;align-items:center;justify-content:center}
</style>
</head>
<body>

<!-- hero background -->
<svg class="hero-bg" width="1200" height="760" viewBox="0 0 1200 760" aria-hidden="true">
  <defs>
    <linearGradient id="heroGlow" x1="0" y1="0" x2="1" y2="0">
      <stop offset="0" stop-color="#15151a"/>
      <stop offset="0.6" stop-color="#1b1b22"/>
      <stop offset="1" stop-color="#5a0c22"/>
    </linearGradient>
  </defs>
  <path d="M0 700 C20 740 80 760 160 760 L175 740 Z" fill="#e4e4e6"/>
  <path d="M0 0 H1200 V500 C950 600 700 650 420 690 C250 712 90 720 0 620 Z" fill="url(#heroGlow)"/>
</svg>
<div class="hero-photo" role="img" aria-label="Soldier in camouflage operating a holographic tablet display"></div>

<header class="site-header">
  <div class="brand"><span>VKTO MERIDIAN</span><span class="brand-mark"></span></div>
  <nav class="main-nav">
    <a class="active">HOME</a><a>ABOUT</a><a>WORK WITH US</a><a>ON ORBIT</a><a>NEWS</a><a>CONTACT US</a>
  </nav>
  <div class="search-btn">
    <svg width="38" height="38" viewBox="0 0 38 38" aria-hidden="true"><circle cx="18" cy="18" r="5" fill="none" stroke="#fff" stroke-width="1.6"/><line x1="21.5" y1="21.5" x2="25" y2="25" stroke="#fff" stroke-width="1.6"/></svg>
  </div>
</header>

<section class="hero-copy">
  <h1 class="hero-title"><span class="red">VKTO</span><br><span class="white">MERIDIAN</span></h1>
  <p class="hero-sub">DEFENSE AND FEDERAL SPACE</p>
  <p class="hero-text">Aenean sollicitudin, lorem quis bibendum auctor nisi elit consequat ipsum nec sagittis sem</p>
  <a class="btn btn-red">JOIN THE MISSION</a>
</section>

<!-- about -->
<div class="about-frame">
  <div class="about-photo" role="img" aria-label="Soldier wearing a virtual reality headset interacting with holographic interface"></div>
</div>
<section class="about-copy">
  <p class="eyebrow">ABOUT US</p>
  <h2 class="display section-title-left">INTELLIGENCE<br>ANALYSIS...</h2>
  <p class="about-text">Aenean sollicitudin lorem quis bibendum auctor nisi elit consequat ipsum, nec sagittis sem nibh id elit. Duis sed odio sit amet nibh vulputate cursus a sit amet mauris. Morbi accumsan ipsum velit. Nam nec tellus a odio tincidunt auctor a ornare odio. Sed non mauris vitae erat...</p>
  <a class="btn btn-grey">FIND OUT MORE</a>
</section>

<!-- applications -->
<h2 class="display section-title" style="top:1290px">APPLICATIONS</h2>
<div class="app-accent"></div>
<article class="app-card" style="left:88px">
  <div class="app-photo" role="img" aria-label="Communication satellite orbiting above Earth" style="background:linear-gradient(180deg,#0b1020,#1d3050 55%,#b98a5a 75%,#2a2a30)"></div>
  <div class="app-body"><h3 class="app-name">COMMUNICATION</h3><p class="app-text">We focus on efficiency and results in operations, so you can develop and promote your...</p><a class="read-more">READ MORE</a></div>
</article>
<article class="app-card" style="left:347px">
  <div class="app-photo" role="img" aria-label="Air defense missile launcher system" style="background:linear-gradient(180deg,#9fb3c4,#c9ced2 55%,#4a4d52)"></div>
  <div class="app-body"><h3 class="app-name">DEFENSE EW</h3><p class="app-text">We focus on efficiency and results in operations, so you can develop and promote your...</p><a class="read-more">READ MORE</a></div>
</article>
<article class="app-card" style="left:606px">
  <div class="app-photo" role="img" aria-label="Soldier hands on steering wheel inside military vehicle" style="background:linear-gradient(135deg,#c4b79a,#6c6656 50%,#2c2c2e)"></div>
  <div class="app-body"><h3 class="app-name">DEFENSE ISR</h3><p class="app-text">We focus on efficiency and results in operations, so you can develop and promote your...</p><a class="read-more">READ MORE</a></div>
</article>
<article class="app-card" style="left:865px">
  <div class="app-photo" role="img" aria-label="Radar tower against a cloudy sky" style="background:linear-gradient(180deg,#8fa9b6,#b8c8cf 60%,#5d6e58)"></div>
  <div class="app-body"><h3 class="app-name">RADAR</h3><p class="app-text">We focus on efficiency and results in operations, so you can develop and promote your...</p><a class="read-more">READ MORE</a></div>
</article>
<div class="slider-btn" style="left:782px"><svg width="32" height="38" aria-hidden="true"><path d="M18 15 L14 19 L18 23" fill="none" stroke="#fff" stroke-width="1.5"/></svg></div>
<div class="slider-track"></div>
<div class="slider-btn" style="left:1113px"><svg width="32" height="38" aria-hidden="true"><path d="M14 15 L18 19 L14 23" fill="none" stroke="#fff" stroke-width="1.5"/></svg></div>

<!-- banner -->
<section class="banner" role="img" aria-label="Large satellite radio dish standing on a grassy plain under a blue sky">
  <svg class="abs" style="left:0;bottom:0" width="1200" height="743" viewBox="0 0 1200 743" aria-hidden="true">
    <path d="M0 440 C300 560 650 720 1200 580 V743 H0 Z" fill="#e6e6e8"/>
    <path d="M0 468 C300 600 700 760 1180 600 L1200 743 H0 Z" fill="#ffffff"/>
  </svg>
</section>
<h2 class="banner-title">DEFENSE<br>AND FEDERAL<br>SPACE...</h2>
<p class="banner-sub">DELIVERING BATTLEFIELD DATA WHERE<br>AND WHEN IT'S NEEDED</p>
<a class="btn btn-white">GET STARTED</a>

<!-- work with us -->
<h2 class="display section-title" style="top:2616px">WORK WITH US</h2>
<p class="work-text">Aenean sollicitudin lorem quis bibendum auctor nisi elit consequat ipsum, nec sagittis sem nibh id elit duis sed odio sit amet nibh vulputate cursus</p>
<div class="work-item" style="left:311px">
  <div class="work-circle red">
    <svg width="70" height="70" viewBox="0 0 70 70" aria-hidden="true" fill="#fff"><circle cx="28" cy="18" r="9"/><path d="M12 52 C12 36 20 30 28 30 C36 30 44 36 44 52 Z"/><path d="M34 58 L46 44 L52 50 L62 38" fill="none" stroke="#fff" stroke-width="3"/><text x="46" y="26" font-family="Poppins,sans-serif" font-size="16" font-weight="700">$</text></svg>
  </div>
  <p class="work-label">SMALL<br>BUSINESS</p>
</div>
<div class="work-item" style="left:506px">
  <div class="work-circle dark">
    <svg width="70" height="70" viewBox="0 0 70 70" aria-hidden="true" fill="#fff"><circle cx="35" cy="30" r="6"/><path d="M26 46 C26 38 44 38 44 46 Z"/><path d="M35 8 L31 14 H39 Z M35 62 L31 56 H39 Z M8 35 L14 31 V39 Z M62 35 L56 31 V39 Z M15 15 L22 17 L17 22 Z M55 15 L48 17 L53 22 Z M15 55 L17 48 L22 53 Z M55 55 L53 48 L48 53 Z"/></svg>
  </div>
  <p class="work-label">OUR<br>OPPORTUNITIES</p>
</div>
<div class="work-item" style="left:699px">
  <div class="work-circle red">
    <svg width="70" height="70" viewBox="0 0 70 70" aria-hidden="true"><circle cx="30" cy="30" r="17" fill="none" stroke="#fff" stroke-width="5"/><line x1="42" y1="42" x2="58" y2="58" stroke="#fff" stroke-width="7" stroke-linecap="round"/><rect x="22" y="25" width="16" height="11" rx="2" fill="#fff"/><rect x="27" y="22" width="6" height="4" fill="none" stroke="#fff" stroke-width="2"/></svg>
  </div>
  <p class="work-label">OUR<br>CAREERS</p>
</div>
<div class="divider"></div>

<!-- blog -->
<h2 class="display section-title" style="top:3043px">LATEST BLOG</h2>
<article class="blog-card" style="left:165px">
  <div class="blog-photo" role="img" aria-label="Soldier with rifle wearing a virtual reality headset in blue light" style="background:linear-gradient(160deg,#2a3f8a,#5f86c8 50%,#1c2344)"></div>
  <div class="blog-body"><p class="blog-date">25-05-2022</p><h3 class="blog-title">Some blog heading goes...</h3><p class="blog-text">Aenean sollicitudin lorem quis bibendum auctor nisi elit consequat ipsum, nec sagittis sem...</p><a class="blog-link">VIEW DETAIL</a></div>
</article>
<article class="blog-card" style="left:461px">
  <div class="blog-photo" role="img" aria-label="Radar dome on a tower under a cloudy sky" style="background:linear-gradient(180deg,#4f7fb0,#c8d4de 55%,#5a6470)"></div>
  <div class="blog-body"><p class="blog-date">25-05-2022</p><h3 class="blog-title">Some blog heading goes...</h3><p class="blog-text">Aenean sollicitudin lorem quis bibendum auctor nisi elit consequat ipsum, nec sagittis sem...</p><a class="blog-link">VIEW DETAIL</a></div>
</article>
<article class="blog-card" style="left:756px">
  <div class="blog-photo" role="img" aria-label="Soldier in headset touching a holographic interface" style="background:linear-gradient(160deg,#8fb0c8,#4c6a80 50%,#c8a060 80%,#2a3038)"></div>
  <div class="blog-body"><p class="blog-date">25-05-2022</p><h3 class="blog-title">Some blog heading goes...</h3><p class="blog-text">Aenean sollicitudin lorem quis bibendum auctor nisi elit consequat ipsum, nec sagittis sem...</p><a class="blog-link">VIEW DETAIL</a></div>
</article>

<!-- newsletter -->
<section class="newsletter">
  <h2 class="newsletter-title">SUBSCRIBE<br>NEWSLETTER</h2>
  <p class="newsletter-text">Join our subscribers list go get the latest news.</p>
  <div class="subscribe-form">
    <div class="subscribe-input">
      <svg class="abs" style="left:16px;top:3px" width="16" height="12" viewBox="0 0 16 12" aria-hidden="true"><rect x="0.5" y="0.5" width="15" height="11" fill="none" stroke="#9a9ca0"/><path d="M1 1 L8 7 L15 1" fill="none" stroke="#9a9ca0"/></svg>
      Enter your email address...
    </div>
    <div class="subscribe-btn">SUBSCRIBE</div>
  </div>
</section>

<!-- footer -->
<svg class="footer-bg" width="1200" height="620" viewBox="0 0 1200 620" aria-hidden="true">
  <path d="M0 20 C300 40 560 60 780 110 L1200 180 V620 H0 Z" fill="#111114"/>
</svg>
<div class="footer-brand"><span>VKTO MERIDIAN</span><span class="brand-mark"></span></div>
<div class="footer-col" style="left:439px">
  <h4 class="footer-head">AGENCY LINKS</h4>
  <ul class="footer-links">
    <li>CTO</li><li>Defense Portal</li><li>Agency Review Office</li><li>Workplace Rights Notice</li><li>Freedom of Information</li><li>External Links Disclaimer</li><li>Privacy &amp; Security</li><li>Web Policy</li><li>Accessibility/Section 508</li>
  </ul>
</div>
<div class="footer-col" style="left:669px">
  <h4 class="footer-head">CONTACT INFO</h4>
  <div class="contact-item"><svg width="14" height="11" viewBox="0 0 14 11" aria-hidden="true"><rect width="14" height="11" fill="#c8002f"/><path d="M0 0 L7 6 L14 0" fill="none" stroke="#111" stroke-width="1.2"/></svg>Email:<br>info@example.com</div>
  <div class="contact-item"><svg width="14" height="14" viewBox="0 0 14 14" aria-hidden="true"><path d="M3 1 L5.5 4 L4 6 C5 8 6 9 8 10 L10 8.5 L13 11 L11 13 C6 13 1 8 1 3 Z" fill="#c8002f"/></svg>Phone:<br>+08 123 456 7890</div>
  <div class="contact-item"><svg width="12" height="15" viewBox="0 0 12 15" aria-hidden="true"><path d="M6 0 C2.7 0 0 2.6 0 5.8 C0 10 6 15 6 15 C6 15 12 10 12 5.8 C12 2.6 9.3 0 6 0 Z" fill="#c8002f"/><circle cx="6" cy="5.8" r="2" fill="#111"/></svg>Location:<br>Some address line goes<br>here city name country</div>
</div>
<div class="footer-col" style="left:890px">
  <h4 class="footer-head">SOCIAL MEDIA</h4>
  <div class="socials"><span class="social"></span><span class="social"></span><span class="social"></span><span class="social"></span></div>
</div>
<div class="footer-rule"></div>
<p class="copyright">© Copyright 2022 | All Rights Reserved</p>
<div class="chat-btn">
  <svg width="26" height="24" viewBox="0 0 26 24" aria-hidden="true"><path d="M3 3 H23 V16 H10 L5 21 V16 H3 Z" fill="#fff"/><circle cx="9" cy="9.5" r="1.5" fill="#c8002f"/><circle cx="13" cy="9.5" r="1.5" fill="#c8002f"/><circle cx="17" cy="9.5" r="1.5" fill="#c8002f"/></svg>
</div>

</body>
</html>
```